Design my New and Engaging Wix Website

We just recently started a new website for HARMONY LEARNING (www.harmony-learning.example) and would like to have a custom design for it. The design should be engaging and modern. You can use our logo and design the website inspired by the style.

```html
<!DOCTYPE html>
<html lang="en">
<head>
<meta charset="utf-8">
<title>Harmony Learning</title>
<link rel="stylesheet" href="https://fonts.googleapis.com/css2?family=Nunito+Sans:wght@800&family=Raleway:wght@400;700&display=swap">
<style>
  :root {
    --brand-blue: #1a87c5;
    --mark-blue: #1a98dc;
    --ink: #111111;
    --header-bg: #ffffff;
    --hero-bg: #f2faf9;
  }
  * { margin: 0; padding: 0; box-sizing: border-box; }
  html, body {
    width: 1200px;
    height: 552px;
    overflow: hidden;
    background: var(--hero-bg);
  }
  .page {
    position: relative;
    width: 1200px;
    height: 552px;
    overflow: hidden;
  }
  .site-header {
    position: absolute;
    top: 0; left: 0;
    width: 1200px;
    height: 114px;
    background: var(--header-bg);
  }
  .brand {
    position: absolute;
    left: 78px;
    top: 30px;
    display: flex;
    align-items: center;
    gap: 22px;
  }
  .brand-dot {
    width: 44px;
    height: 44px;
    border-radius: 50%;
    background: var(--mark-blue);
  }
  .brand-name {
    font-family: "Raleway", sans-serif;
    font-weight: 400;
    font-size: 21px;
    letter-spacing: 0.2px;
    color: var(--ink);
  }
  .main-nav {
    position: absolute;
    top: 39px;
    left: 1034px;
    display: flex;
    gap: 19px;
    font-family: "Raleway", sans-serif;
    font-weight: 400;
    font-size: 13px;
  }
  .main-nav a {
    color: var(--ink);
    text-decoration: none;
  }
  .hero {
    position: absolute;
    top: 114px; left: 0;
    width: 1200px;
    height: 438px;
    background: var(--hero-bg);
  }
  .hero-title {
    position: absolute;
    left: 149px;
    top: 114px;
    font-family: "Nunito Sans", sans-serif;
    font-weight: 800;
    font-size: 72px;
    line-height: 86px;
    letter-spacing: 0.5px;
    text-transform: uppercase;
    color: var(--brand-blue);
    white-space: nowrap;
  }
  .hero-title span { display: block; }
  .section-heading {
    position: absolute;
    left: 151px;
    top: 399px;
    font-family: "Raleway", sans-serif;
    font-weight: 700;
    font-size: 19px;
    color: var(--ink);
  }
</style>
</head>
<body>
<div class="page">
  <header class="site-header">
    <div class="brand">
      <span class="brand-dot" aria-hidden="true"></span>
      <span class="brand-name">HARMONY LEARNING</span>
    </div>
    <nav class="main-nav">
      <a href="#">Start</a>
      <a href="#">Kunden</a>
    </nav>
  </header>
  <section class="hero">
    <h1 class="hero-title">
      <span>Qualitative and</span>
      <span>accessible peace</span>
      <span>education resources</span>
    </h1>
    <h2 class="section-heading">Our Mission and Contribution</h2>
  </section>
</div>
</body>
</html>
```